Business card design needed

It's a new business in town.Something so the name stands out.I need a logo for the B.R.K
I may all so use the design as a sign on a building

Contact Information for Business Card

B.R.K
Brackenvale Auto Detailing
42 Tillbury Crs
Brackenvale Vic 3819
Ph:(03)58264027
Mob:0417392658

```html
<!DOCTYPE html>
<html lang="en">
<head>
<meta charset="UTF-8">
<title>Brackenvale Auto Detailing — Business Card</title>
<link rel="stylesheet" href="https://fonts.googleapis.com/css2?family=Teko:wght@400;500&display=swap">
<style>
  :root {
    --page-bg: #ffffff;
    --card-bg: #ffffff;
    --brand-blue: #2a8af0;
    --mark-blue: #36a6f7;
    --ghost-tint: #eefcfc;
    --card-edge: #e3e6e8;
  }
  * { margin: 0; padding: 0; box-sizing: border-box; }
  html, body {
    width: 1200px;
    height: 1000px;
    overflow: hidden;
    background: var(--page-bg);
  }
  .business-card {
    position: absolute;
    left: 70px;
    top: 167px;
    width: 1052px;
    height: 611px;
    background: var(--card-bg);
    border: 1px solid var(--card-edge);
    overflow: hidden;
    font-family: "Teko", "Arial Narrow", sans-serif;
    color: var(--brand-blue);
  }
  .ghost-name {
    position: absolute;
    left: 712px;
    top: 10px;
    font-size: 230px;
    font-weight: 500;
    line-height: 1;
    color: var(--ghost-tint);
    white-space: nowrap;
    user-select: none;
    z-index: 0;
  }
  .brand-mark {
    position: absolute;
    left: 78px;
    top: 154px;
    width: 175px;
    height: 310px;
    display: flex;
    align-items: center;
    justify-content: center;
    z-index: 1;
  }
  .brand-mark__name {
    font-size: 118px;
    font-weight: 500;
    line-height: 1;
    color: var(--mark-blue);
    letter-spacing: 1px;
    white-space: nowrap;
  }
  .contact-block {
    position: absolute;
    left: 432px;
    top: 302px;
    z-index: 1;
    text-transform: uppercase;
    font-weight: 400;
    font-size: 46px;
    line-height: 1;
    white-space: nowrap;
    transform: scaleX(0.86);
    transform-origin: left top;
  }
  .contact-block__address { margin-top: 26px; }
  .contact-block__phones {
    display: flex;
    align-items: center;
    margin-top: 4px;
  }
  .phone-icon { width: 70px; height: 44px; margin-right: 30px; fill: var(--brand-blue); }
  .mobile-icon { width: 60px; height: 44px; margin: 0 24px 0 20px; }
  .phone-number { padding-top: 6px; }
</style>
</head>
<body>
  <section class="business-card">
    <div class="ghost-name" aria-hidden="true">B.R.K</div>

    <div class="brand-mark">
      <span class="brand-mark__name">B.R.K</span>
    </div>

    <div class="contact-block">
      <p class="contact-block__business">Brackenvale Auto Detailing</p>
      <p class="contact-block__address">42 Tillbury Crs Brackenvale Vic 3819</p>
      <p class="contact-block__phones">
        <svg class="phone-icon" viewBox="0 0 70 44" aria-label="Phone">
          <path d="M4 24 L52 6 Q62 2 66 10 Q68 16 62 19 L56 21 Q52 22 50 18 L48 15 L20 26 L22 30 Q24 34 19 37 L12 40 Q4 42 2 33 Q1 27 4 24 Z"/>
        </svg>
        <span class="phone-number">03 58264027</span>
        <svg class="mobile-icon" viewBox="0 0 60 44" aria-label="Mobile">
          <g transform="rotate(-22 30 22)">
            <rect x="6" y="10" width="48" height="24" rx="5" fill="var(--brand-blue)"/>
            <rect x="13" y="14" width="34" height="16" rx="1.5" fill="#ffffff"/>
            <circle cx="9.5" cy="22" r="1.8" fill="#ffffff"/>
          </g>
        </svg>
        <span class="phone-number">0417392658</span>
      </p>
    </div>
  </section>
</body>
</html>
```